Modern and Vibrant Car Wash Website

In Summary: A website using our Menus for Exterior and Full Service Car Washes: Meadowlark, tidewater car wash, Vireo and Copperleaf Express Car Wash websites (link attached below are good references for the type of cartoony fun design).

I will add our flyer, and menus, and some other graphics as a visual reference. Will over time add the files (AI and SVG so you can use them).

Car wash front page should be nice and clean. I have lots of videos and photos we can use throughout the wash. Would like a video on the landing page.

Our shop section can remain blank as my POS developers will create a hyperlink to it.

Main easy to use functions should be the Car Wash services, their price and full service ones as well. Allow customers to see, book if needed etc.

Please note I have the website on PLOM.

I have attached a general pdf as well for some more info.

https://meadowlarkgleamwash.ca/
https://tidewatercarwash.ca/
https://marblecarwash.com/
https://vireowash.com/
https://plainpagebuilder.com/carwash-website-design/
https://copperleafexpresscarwash.com/

```html
<!DOCTYPE html>
<html lang="en">
<head>
<meta charset="utf-8">
<title>Meadowlark Super Wash</title>
<link rel="stylesheet" href="https://fonts.googleapis.com/css2?family=Baloo+2:wght@700;800&family=Poppins:wght@400;500;600;700;800&display=swap">
<style>
:root{
  --blue:#0b6fc4;
  --blue-dark:#0a3f7a;
  --blue-light:#2f8fe0;
  --yellow:#f7c61d;
  --ink:#14213d;
  --muted:#5d6b80;
  --pale:#eef3f9;
  --white:#ffffff;
  --line:#d9e2ee;
}
*{box-sizing:border-box;margin:0;padding:0}
html,body{width:1200px;height:5176px;overflow:hidden}
body{position:relative;font-family:"Poppins",sans-serif;color:var(--ink);background:var(--white);font-size:13px;line-height:1.6}
.display{font-family:"Baloo 2","Poppins",sans-serif;font-weight:800;text-transform:uppercase;letter-spacing:.5px;line-height:1.02}
.abs{position:absolute}
.ph{position:absolute;display:block}
.btn{display:inline-block;border-radius:30px;font-weight:600;font-size:11px;text-transform:uppercase;padding:11px 24px;letter-spacing:.4px}
.btn-yellow{background:var(--yellow);color:var(--ink)}
.btn-outline{border:2px solid var(--white);color:var(--white)}
.btn-blue{background:var(--blue);color:var(--white)}
.section-title{position:absolute;left:0;width:1200px;text-align:center;font-size:36px;color:var(--ink)}
.section-title::after{content:"";display:block;width:60px;height:4px;border-radius:2px;background:var(--yellow);margin:10px auto 0}
.wave{position:absolute;left:0;width:1200px}

/* Hero */
.hero{top:0;left:0;width:1200px;height:940px;overflow:hidden}
.hero-bg{inset:0;background:linear-gradient(100deg,#0d1e33 0%,#1d3452 40%,#4f6580 70%,#8ea2b8 100%)}
.hero-shade{position:absolute;inset:0;background:linear-gradient(90deg,rgba(5,15,30,.75) 0%,rgba(5,15,30,.2) 60%,rgba(0,0,0,0) 100%)}
.brand{top:14px;left:40px;width:190px;height:74px;background:var(--white);border-radius:40px;display:flex;align-items:center;justify-content:center;gap:8px;box-shadow:0 4px 12px rgba(0,0,0,.2)}
.brand .dot{width:16px;height:16px;border-radius:50%;background:var(--yellow)}
.brand span{font-weight:700;font-size:17px;color:var(--blue)}
.topinfo{top:12px;left:420px;display:flex;gap:56px;color:var(--white);font-size:10px;line-height:1.3}
.topinfo div{display:flex;gap:8px;align-items:center}
.topinfo b{display:block;color:var(--yellow);font-size:11px}
.topinfo svg{width:22px;height:22px;flex:none}
.nav{top:52px;left:250px;width:690px;height:38px;background:var(--white);border-radius:20px;display:flex;align-items:center;padding:0 20px;gap:30px;font-size:11px;font-weight:600;text-transform:uppercase}
.nav .active{background:var(--yellow);padding:5px 14px;border-radius:14px}
.nav .icons{margin-left:auto;display:flex;gap:14px}
.nav svg{width:15px;height:15px}
.get-touch{top:52px;left:960px;height:38px;line-height:16px}
.hero-copy{top:240px;left:70px;width:620px;color:var(--white)}
.hero-copy h1{font-size:62px}
.hero-copy p{margin-top:24px;font-size:12px;width:340px;color:#dce6f3}
.hero-actions{margin-top:30px;display:flex;gap:16px}

/* About */
.about{top:940px;left:0;width:1200px;height:400px}
.collage-a{left:220px;top:40px;width:130px;height:150px;border-radius:60px 10px 60px 10px;background:linear-gradient(135deg,#5e7590,#c3ced9)}
.collage-b{left:360px;top:10px;width:140px;height:110px;border-radius:10px 60px 10px 60px;background:linear-gradient(135deg,#1d5fa0,#8fb6dc)}
.collage-c{left:180px;top:200px;width:150px;height:120px;border-radius:10px 60px 10px 60px;background:linear-gradient(135deg,#2e6aa7,#e3c553)}
.collage-d{left:350px;top:130px;width:140px;height:190px;border-radius:60px;background:linear-gradient(180deg,#3ba03f,#20602a)}
.about-copy{left:640px;top:30px;width:450px}
.about-copy h2{font-size:24px;color:var(--ink)}
.about-copy p{margin-top:14px;font-size:11px;color:var(--muted)}
.checks{list-style:none;margin-top:12px}
.checks li{display:flex;gap:8px;font-size:11px;font-weight:500;margin-bottom:8px;align-items:flex-start}
.checks svg{width:14px;height:14px;flex:none;margin-top:2px}

/* Full service */
.full{top:1340px;left:0;width:1200px;height:780px;background:var(--pale)}
.tabs{top:118px;left:0;width:1200px;display:flex;justify-content:center;gap:20px;font-size:11px;font-weight:600}
.tabs .on{background:var(--yellow);padding:6px 22px;border-radius:16px}
.tabs .off{padding:6px 10px;color:var(--muted)}
.service-cards{top:180px;left:200px;display:flex;gap:22px;align-items:center}
.svc{width:150px;height:104px;background:var(--white);border-radius:10px;border:1px solid var(--line);padding:14px 12px;font-size:10px;font-weight:700;text-transform:uppercase;line-height:1.3}
.svc svg{width:28px;height:28px;display:block;margin-bottom:12px}
.svc.hl{background:var(--blue);color:var(--white);height:130px;border:none}
.fundraiser{top:390px;left:190px;width:820px;height:310px;background:var(--blue);border-radius:20px;overflow:hidden}
.fund-copy{left:44px;top:40px;width:350px;color:var(--white)}
.fund-copy h3{font-size:29px}
.fund-copy p{margin-top:14px;font-size:11px;color:#d6e6f7}
.fund-copy .btn{margin-top:22px}
.fund-photo{right:0;top:0;width:420px;height:310px;background:linear-gradient(120deg,#0f2d52,#3b5f8a 55%,#c94437)}

/* Guarantee */
.guarantee{top:2120px;left:0;width:1200px;height:410px}
.guarantee .section-title{top:100px}
.guar-row{top:210px;left:180px;display:flex;gap:60px}
.guar-item{width:122px;text-align:center;font-size:10px;font-weight:700;text-transform:uppercase;line-height:1.3}
.guar-circle{width:110px;height:110px;border-radius:50%;margin:0 auto 14px;border:4px solid var(--white);box-shadow:0 0 0 2px var(--line)}

/* Champion */
.champion{top:2530px;left:0;width:1200px;height:530px;background:var(--blue);overflow:hidden}
.champion .stripe{position:absolute;top:0;left:330px;width:560px;height:530px;background:var(--blue-light);opacity:.35;transform:skewX(-12deg)}
.champion h2{position:absolute;top:80px;width:1200px;text-align:center;color:var(--white);font-size:36px}
.truck{left:340px;top:150px;width:520px;height:290px;background:var(--white);border-radius:8px;overflow:hidden}
.truck .ph{inset:14px;background:linear-gradient(180deg,#e9edf1,#9aa6b3 60%,#3c4550)}
.feature{top:170px;width:270px;color:var(--white)}
.feature h4{font-size:18px;color:var(--yellow)}
.feature p{margin-top:8px;font-size:10px;color:#d6e6f7}
.feature svg{width:34px;height:34px;display:block;margin-bottom:8px}
.feature.left{left:50px}
.feature.right{left:880px;text-align:right}
.feature.right svg{margin-left:auto}

/* Washbooks */
.washbooks{top:3060px;left:0;width:1200px;height:640px}
.washbooks .section-title{top:60px}
.plans{top:150px;left:195px;display:flex;gap:20px;align-items:flex-start}
.plan{width:256px;background:var(--white);border-radius:12px;border:1px solid var(--line);overflow:hidden;box-shadow:0 6px 18px rgba(10,63,122,.08)}
.plan-head{background:var(--pale);padding:18px 20px 14px}
.plan-head h3{font-size:21px;color:var(--blue);white-space:nowrap}
.plan-head small{font-size:9px;font-weight:700;text-transform:uppercase;color:var(--muted)}
.plan-price{display:flex;justify-content:space-between;align-items:center;padding:14px 20px;border-bottom:1px solid var(--line)}
.plan-price b{font-size:18px}
.plan-price span{border:1px solid var(--line);border-radius:14px;padding:3px 12px;font-size:10px;font-weight:600}
.plan ul{list-style:none;padding:16px 20px 20px}
.plan li{display:flex;gap:8px;font-size:10px;color:var(--muted);margin-bottom:12px}
.plan li svg{width:12px;height:12px;flex:none;margin-top:2px}
.plan.featured{margin-top:-24px}
.plan.featured .plan-head{background:var(--blue)}
.plan.featured .plan-head h3,.plan.featured .plan-head small{color:var(--white)}

/* Contact */
.contact{top:3700px;left:0;width:1200px;height:560px;background:var(--pale)}
.contact-photo{left:70px;top:40px;width:360px;height:500px;background:linear-gradient(180deg,#d7dde4,#5b6f86 70%,#1b3a63);border-radius:0 0 180px 180px}
.contact h2{left:660px;top:70px;width:470px;font-size:26px;white-space:nowrap}
.form{left:660px;top:130px;width:420px;display:grid;grid-template-columns:1fr 1fr;gap:12px}
.field{height:38px;background:var(--white);border:1px solid var(--line);border-radius:4px;padding:10px 12px;font-size:10px;color:var(--muted)}
.field.area{grid-column:1/3;height:110px}
.form .btn{grid-column:1/2;width:110px;text-align:center}

/* Testimonial */
.testimonial{top:4260px;left:0;width:1200px;height:440px}
.testimonial .section-title{top:30px}
.quotes{top:130px;left:210px;display:flex;gap:20px}
.quote{width:380px;background:var(--white);border-radius:10px;padding:22px 24px;box-shadow:0 6px 20px rgba(10,63,122,.12);position:relative;border-bottom:4px solid var(--blue)}
.quote-top{display:flex;gap:12px;align-items:center}
.avatar{width:46px;height:46px;border-radius:50%;background:linear-gradient(135deg,#b8c6d6,#6f8399);flex:none}
.quote h5{font-size:16px;color:var(--blue)}
.quote small{font-size:9px;color:var(--muted)}
.quote p{margin-top:14px;font-size:10px;color:var(--muted)}
.quote svg{position:absolute;right:22px;top:22px;width:32px;height:26px}

/* Footer */
.footer{top:4700px;left:0;width:1200px;height:476px;background:var(--blue)}
.foot-contact{top:86px;left:0;width:1200px;display:flex;justify-content:center;gap:110px;color:var(--white);font-size:10px;line-height:1.3}
.foot-contact div{display:flex;gap:8px;align-items:center}
.foot-contact b{display:block;color:var(--yellow);font-size:11px}
.foot-contact svg{width:24px;height:24px}
.foot-rule{top:140px;left:120px;width:960px;height:1px;background:rgba(255,255,255,.25)}
.foot-brand{top:190px;left:120px;width:170px;height:70px;background:var(--white);border-radius:36px;display:flex;align-items:center;justify-content:center;gap:8px}
.foot-brand .dot{width:14px;height:14px;border-radius:50%;background:var(--yellow)}
.foot-brand span{font-weight:700;font-size:15px;color:var(--blue)}
.foot-col{top:170px;color:var(--white);font-size:10px}
.foot-col h6{font-size:12px;font-weight:700;margin-bottom:12px;color:var(--yellow);text-transform:uppercase}
.foot-col li{list-style:none;margin-bottom:4px;color:#d6e6f7}
.post{display:flex;gap:10px;margin-bottom:14px;width:210px}
.post .thumb{width:48px;height:40px;border-radius:4px;background:linear-gradient(135deg,#6f8fb3,#203f66);flex:none}
.post small{display:block;color:var(--yellow);font-size:9px}
.copyright{bottom:0;left:0;width:1200px;height:38px;background:var(--blue-dark);color:#c9d9ec;font-size:10px;text-align:center;line-height:38px}
</style>
</head>
<body>

<!-- Hero -->
<header class="abs hero">
  <div class="ph hero-bg" role="img" aria-label="Photo of a man pressure-washing a dark car, with a cartoon boy washing a toy car at the right"><div class="hero-shade"></div></div>
  <div class="abs brand"><i class="dot"></i><span>Meadowlark</span></div>
  <div class="abs topinfo">
    <div><svg viewBox="0 0 24 24"><circle cx="12" cy="12" r="12" fill="#f7c61d"/><path d="M8 6l2 0 1 3-1.5 1a7 7 0 0 0 4 4l1-1.5 3 1 0 2a2 2 0 0 1-2 2A10 10 0 0 1 6 8a2 2 0 0 1 2-2z" fill="#14213d"/></svg><span><b>Call Us</b>(587) 240-1186</span></div>
    <div><svg viewBox="0 0 24 24"><circle cx="12" cy="12" r="12" fill="#f7c61d"/><rect x="6" y="8" width="12" height="9" rx="1" fill="none" stroke="#14213d" stroke-width="1.6"/><path d="M6 8l6 5 6-5" fill="none" stroke="#14213d" stroke-width="1.6"/></svg><span><b>Email Us</b>hello@meadowlarkgleamwash.ca</span></div>
    <div><svg viewBox="0 0 24 24"><circle cx="12" cy="12" r="12" fill="#f7c61d"/><path d="M12 5a4.5 4.5 0 0 1 4.5 4.5c0 3.5-4.5 9-4.5 9s-4.5-5.5-4.5-9A4.5 4.5 0 0 1 12 5z" fill="#14213d"/><circle cx="12" cy="9.5" r="1.6" fill="#f7c61d"/></svg><span><b>Locations</b>1420 Larkspur Rd, Fairview</span></div>
  </div>
  <nav class="abs nav">
    <span>Home</span><span class="active">Services</span><span>Portfolio</span><span>Pages</span><span>News</span><span>Contact</span>
    <span class="icons">
      <svg viewBox="0 0 16 16"><circle cx="7" cy="7" r="5" fill="none" stroke="#14213d" stroke-width="2"/><path d="M11 11l4 4" stroke="#14213d" stroke-width="2"/></svg>
      <svg viewBox="0 0 16 16"><path d="M1 2h3l2 8h8l1-6H5" fill="none" stroke="#14213d" stroke-width="1.6"/><circle cx="7" cy="13.5" r="1.3" fill="#14213d"/><circle cx="13" cy="13.5" r="1.3" fill="#14213d"/></svg>
    </span>
  </nav>
  <a class="abs btn btn-blue get-touch">Get In Touch</a>
  <div class="abs hero-copy">
    <h1 class="display">Get A Brilliant<br>Clean Every Time</h1>
    <p>With 9 car wash locations offering a variety of services, we make it easy for your car to look its best. Explore our membership options and start saving today!</p>
    <div class="hero-actions"><a class="btn btn-yellow">Find a Location</a><a class="btn btn-outline">Download the App</a></div>
  </div>
  <svg class="wave" style="top:860px" width="1200" height="80" viewBox="0 0 1200 80" preserveAspectRatio="none"><path d="M0 40 C200 0 400 70 600 36 S1000 0 1200 34 V80 H0Z" fill="#ffffff"/></svg>
</header>

<!-- About -->
<section class="abs about">
  <div class="ph collage-a" role="img" aria-label="Photo of a worker washing a car"></div>
  <div class="ph collage-b" role="img" aria-label="Photo of a car in the wash tunnel"></div>
  <div class="ph collage-c" role="img" aria-label="Photo of a yellow car being cleaned"></div>
  <div class="ph collage-d" role="img" aria-label="Cartoon mascot holding a sign"></div>
  <div class="abs about-copy">
    <h2 class="display">Canada's most complete car cleaning and detailing service</h2>
    <p>Whatever cleaning service your car requires, we've got it. At Meadowlark Super Wash, all we want is for you to drive that new car feeling every time you start your key in the ignition.</p>
    <ul class="checks">
      <li><svg viewBox="0 0 14 14"><circle cx="7" cy="7" r="7" fill="#f7c61d"/><path d="M4 7l2 2 4-4" fill="none" stroke="#14213d" stroke-width="1.6"/></svg>Tunnel Wash (with state-of-the-art equipment)</li>
      <li><svg viewBox="0 0 14 14"><circle cx="7" cy="7" r="7" fill="#f7c61d"/><path d="M4 7l2 2 4-4" fill="none" stroke="#14213d" stroke-width="1.6"/></svg>Full &amp; Express Detailing</li>
      <li><svg viewBox="0 0 14 14"><circle cx="7" cy="7" r="7" fill="#f7c61d"/><path d="M4 7l2 2 4-4" fill="none" stroke="#14213d" stroke-width="1.6"/></svg>Self-serve Bays</li>
      <li><svg viewBox="0 0 14 14"><circle cx="7" cy="7" r="7" fill="#f7c61d"/><path d="M4 7l2 2 4-4" fill="none" stroke="#14213d" stroke-width="1.6"/></svg>Meadowlark Wash Bars – your one-stop shop for basic car cleaning items and some other fresh-fruit items for your car</li>
      <li><svg viewBox="0 0 14 14"><circle cx="7" cy="7" r="7" fill="#f7c61d"/><path d="M4 7l2 2 4-4" fill="none" stroke="#14213d" stroke-width="1.6"/></svg>Self-serve Pet Wash</li>
    </ul>
  </div>
</section>

<!-- Full service -->
<section class="abs full">
  <svg class="wave" style="top:-30px" width="1200" height="40" viewBox="0 0 1200 40" preserveAspectRatio="none"><path d="M0 40 C300 0 500 30 700 18 S1000 4 1200 20 V40Z" fill="#eef3f9"/></svg>
  <h2 class="section-title display" style="top:40px">Full Service</h2>
  <div class="abs tabs"><span class="on">Express Clean</span><span class="off">Exterior</span></div>
  <div class="abs service-cards">
    <div class="svc"><svg viewBox="0 0 28 28"><rect x="3" y="11" width="22" height="9" rx="3" fill="none" stroke="#0b6fc4" stroke-width="2"/><circle cx="9" cy="21" r="2.5" fill="#0b6fc4"/><circle cx="19" cy="21" r="2.5" fill="#0b6fc4"/><path d="M7 11l3-5h8l3 5" fill="none" stroke="#0b6fc4" stroke-width="2"/></svg>Exterior Hand Dry</div>
    <div class="svc"><svg viewBox="0 0 28 28"><rect x="3" y="11" width="22" height="9" rx="3" fill="none" stroke="#0b6fc4" stroke-width="2"/><circle cx="9" cy="21" r="2.5" fill="#0b6fc4"/><circle cx="19" cy="21" r="2.5" fill="#0b6fc4"/><path d="M7 11l3-5h8l3 5" fill="none" stroke="#0b6fc4" stroke-width="2"/></svg>Express Interior Vacuum</div>
    <div class="svc"><svg viewBox="0 0 28 28"><rect x="3" y="11" width="22" height="9" rx="3" fill="none" stroke="#0b6fc4" stroke-width="2"/><circle cx="9" cy="21" r="2.5" fill="#0b6fc4"/><circle cx="19" cy="21" r="2.5" fill="#0b6fc4"/><path d="M7 11l3-5h8l3 5" fill="none" stroke="#0b6fc4" stroke-width="2"/></svg>Rubber Mats Refresh</div>
    <div class="svc hl"><svg viewBox="0 0 28 28"><rect x="3" y="11" width="22" height="9" rx="3" fill="none" stroke="#ffffff" stroke-width="2"/><circle cx="9" cy="21" r="2.5" fill="#ffffff"/><circle cx="19" cy="21" r="2.5" fill="#ffffff"/><path d="M7 11l3-5h8l3 5" fill="none" stroke="#ffffff" stroke-width="2"/></svg>Door Jambs &amp; Interior Windows Cleaned</div>
    <div class="svc"><svg viewBox="0 0 28 28"><rect x="3" y="11" width="22" height="9" rx="3" fill="none" stroke="#0b6fc4" stroke-width="2"/><circle cx="9" cy="21" r="2.5" fill="#0b6fc4"/><circle cx="19" cy="21" r="2.5" fill="#0b6fc4"/><path d="M7 11l3-5h8l3 5" fill="none" stroke="#0b6fc4" stroke-width="2"/></svg>Interior Glass Cleaned</div>
  </div>
  <div class="abs fundraiser">
    <div class="abs fund-copy">
      <h3 class="display">Launch Your Car Wash Fundraiser to New Heights</h3>
      <p>Enjoy maximum profit with minimal effort when you partner with us. Contact us for your next car wash fundraiser today.</p>
      <a class="btn btn-yellow">Fundraise With Us</a>
    </div>
    <div class="ph fund-photo" role="img" aria-label="Photo of a hand polishing a car with a buffer"></div>
  </div>
</section>

<!-- Guarantee -->
<section class="abs guarantee">
  <h2 class="section-title display">Vireo Clean Car Guarantee®</h2>
  <div class="abs guar-row">
    <div class="guar-item"><div class="guar-circle" role="img" aria-label="Photo of a car covered in foam" style="background:linear-gradient(135deg,#c8d4e2,#44607f)"></div>Double Wash Performance</div>
    <div class="guar-item"><div class="guar-circle" role="img" aria-label="Photo of a worker waxing a car" style="background:linear-gradient(135deg,#d7dde6,#2d4b6d)"></div>Premium Wax Coat</div>
    <div class="guar-item"><div class="guar-circle" role="img" aria-label="Photo of a tire being shined" style="background:linear-gradient(135deg,#90a6be,#1c2d42)"></div>Custom Tire Shine &amp; Wax Polish</div>
    <div class="guar-item"><div class="guar-circle" role="img" aria-label="Photo of a wheel rim being cleaned" style="background:linear-gradient(135deg,#c95040,#3a4050)"></div>Hot-Oiled Rim Cleaning Dry</div>
    <div class="guar-item"><div class="guar-circle" role="img" aria-label="Photo of the underbody flush spray" style="background:linear-gradient(135deg,#8bb0d6,#25507f)"></div>Underbody Flushes</div>
  </div>
</section>

<!-- Champion -->
<section class="abs champion">
  <div class="stripe"></div>
  <h2 class="display">The Champion Treatment</h2>
  <div class="abs truck"><div class="ph" role="img" aria-label="Photo of a pickup truck, half dirty and half clean"></div></div>
  <div class="abs feature left">
    <svg viewBox="0 0 34 34"><circle cx="17" cy="17" r="17" fill="#f7c61d"/><ellipse cx="17" cy="19" rx="6" ry="8" fill="#0a3f7a"/><circle cx="17" cy="10" r="3.5" fill="#0a3f7a"/></svg>
    <h4 class="display">Bug Remover &amp; Pre-Soak</h4>
    <p>Applied prior to every wash, our bug remover and pre-soak break down bugs, road film and dirt so the rest of your wash removes grime easily.</p>
  </div>
  <div class="abs feature right">
    <svg viewBox="0 0 34 34"><circle cx="17" cy="17" r="17" fill="#f7c61d"/><circle cx="13" cy="18" r="5" fill="#0a3f7a"/><circle cx="21" cy="14" r="4" fill="#0a3f7a"/><circle cx="21" cy="22" r="3" fill="#0a3f7a"/></svg>
    <h4 class="display">Foam Bath Wash</h4>
    <p>Our high-foaming wash is rich in lubricants to gently lift dirt, while soft cloth scrubbing leaves every panel clean and bright.</p>
  </div>
  <svg class="wave" style="top:480px" width="1200" height="50" viewBox="0 0 1200 50" preserveAspectRatio="none"><path d="M0 26 C250 0 450 40 700 20 S1050 4 1200 22 V50 H0Z" fill="#ffffff"/></svg>
</section>

<!-- Washbooks -->
<section class="abs washbooks">
  <h2 class="section-title display">Washbooks</h2>
  <div class="abs plans">
    <div class="plan">
      <div class="plan-head"><h3 class="display">Value Shine</h3><small>5 Washes for just</small></div>
      <div class="plan-price"><b>$8.25 EA</b><span>$41.25</span></div>
      <ul>
        <li><svg viewBox="0 0 12 12"><circle cx="6" cy="6" r="6" fill="#f7c61d"/></svg>Lorem ipsum is simply dummy</li>
        <li><svg viewBox="0 0 12 12"><circle cx="6" cy="6" r="6" fill="#f7c61d"/></svg>Lorem ipsum is simply dummy</li>
        <li><svg viewBox="0 0 12 12"><circle cx="6" cy="6" r="6" fill="#f7c61d"/></svg>Lorem ipsum is simply dummy</li>
        <li><svg viewBox="0 0 12 12"><circle cx="6" cy="6" r="6" fill="#f7c61d"/></svg>Lorem ipsum is simply dummy</li>
      </ul>
    </div>
    <div class="plan featured">
      <div class="plan-head"><h3 class="display">Pro Shine</h3><small>5 Washes for just</small></div>
      <div class="plan-price"><b>$10 EA</b><span>$50.00</span></div>
      <ul>
        <li><svg viewBox="0 0 12 12"><circle cx="6" cy="6" r="6" fill="#f7c61d"/></svg>Lorem ipsum is simply dummy</li>
        <li><svg viewBox="0 0 12 12"><circle cx="6" cy="6" r="6" fill="#f7c61d"/></svg>Lorem ipsum is simply dummy</li>
        <li><svg viewBox="0 0 12 12"><circle cx="6" cy="6" r="6" fill="#f7c61d"/></svg>Lorem ipsum is simply dummy</li>
        <li><svg viewBox="0 0 12 12"><circle cx="6" cy="6" r="6" fill="#f7c61d"/></svg>Lorem ipsum is simply dummy</li>
        <li><svg viewBox="0 0 12 12"><circle cx="6" cy="6" r="6" fill="#f7c61d"/></svg>Lorem ipsum is simply dummy</li>
      </ul>
    </div>
    <div class="plan">
      <div class="plan-head"><h3 class="display">Signature Shine</h3><small>5 Washes for just</small></div>
      <div class="plan-price"><b>$12 EA</b><span>$60.00</span></div>
      <ul>
        <li><svg viewBox="0 0 12 12"><circle cx="6" cy="6" r="6" fill="#f7c61d"/></svg>Lorem ipsum is simply dummy</li>
        <li><svg viewBox="0 0 12 12"><circle cx="6" cy="6" r="6" fill="#f7c61d"/></svg>Lorem ipsum is simply dummy</li>
        <li><svg viewBox="0 0 12 12"><circle cx="6" cy="6" r="6" fill="#f7c61d"/></svg>Lorem ipsum is simply dummy</li>
        <li><svg viewBox="0 0 12 12"><circle cx="6" cy="6" r="6" fill="#f7c61d"/></svg>Lorem ipsum is simply dummy</li>
      </ul>
    </div>
  </div>
</section>

<!-- Contact -->
<section class="abs contact">
  <div class="ph contact-photo" role="img" aria-label="Photo of a car wash worker in overalls holding a pressure washer wand"></div>
  <h2 class="abs display">Contact Us Book and Appointment</h2>
  <div class="abs form">
    <div class="field">Your Name</div>
    <div class="field">Your Email</div>
    <div class="field">Your Phone</div>
    <div class="field">Your Service</div>
    <div class="field area">Write Message...</div>
    <a class="btn btn-yellow">Submit</a>
  </div>
</section>

<!-- Testimonial -->
<section class="abs testimonial">
  <h2 class="section-title display">Testimonial</h2>
  <div class="abs quotes">
    <div class="quote">
      <div class="quote-top"><div class="avatar" role="img" aria-label="Customer portrait"></div><div><h5 class="display">Dana Whitlock</h5><small>Customer</small></div></div>
      <svg viewBox="0 0 32 26"><path d="M0 26V14C0 6 4 1 12 0v5c-4 1-6 4-6 8h6v13zM18 26V14c0-8 4-13 12-14v5c-4 1-6 4-6 8h6v13z" fill="#f7c61d"/></svg>
      <p>Many cleaning service providers allow customers to book services online or over the phone. Customers can typically choose the type of service, the date and time of the visit.</p>
    </div>
    <div class="quote">
      <div class="quote-top"><div class="avatar" role="img" aria-label="Customer portrait"></div><div><h5 class="display">Dana Whitlock</h5><small>Customer</small></div></div>
      <svg viewBox="0 0 32 26"><path d="M0 26V14C0 6 4 1 12 0v5c-4 1-6 4-6 8h6v13zM18 26V14c0-8 4-13 12-14v5c-4 1-6 4-6 8h6v13z" fill="#f7c61d"/></svg>
      <p>Many cleaning service providers allow customers to book services online or over the phone. Customers can typically choose the type of service, the date and time of the visit.</p>
    </div>
  </div>
</section>

<!-- Footer -->
<footer class="abs footer">
  <svg class="wave" style="top:0" width="1200" height="50" viewBox="0 0 1200 50" preserveAspectRatio="none"><path d="M0 0 H1200 V20 C1000 44 800 8 600 26 S200 46 0 22Z" fill="#ffffff"/></svg>
  <div class="abs foot-contact">
    <div><svg viewBox="0 0 24 24"><circle cx="12" cy="12" r="12" fill="#f7c61d"/><path d="M8 6l2 0 1 3-1.5 1a7 7 0 0 0 4 4l1-1.5 3 1 0 2a2 2 0 0 1-2 2A10 10 0 0 1 6 8a2 2 0 0 1 2-2z" fill="#14213d"/></svg><span><b>Call Us</b>(587) 240-1186</span></div>
    <div><svg viewBox="0 0 24 24"><circle cx="12" cy="12" r="12" fill="#f7c61d"/><rect x="6" y="8" width="12" height="9" rx="1" fill="none" stroke="#14213d" stroke-width="1.6"/><path d="M6 8l6 5 6-5" fill="none" stroke="#14213d" stroke-width="1.6"/></svg><span><b>Email Us</b>hello@meadowlarkgleamwash.ca</span></div>
    <div><svg viewBox="0 0 24 24"><circle cx="12" cy="12" r="12" fill="#f7c61d"/><path d="M12 5a4.5 4.5 0 0 1 4.5 4.5c0 3.5-4.5 9-4.5 9s-4.5-5.5-4.5-9A4.5 4.5 0 0 1 12 5z" fill="#14213d"/><circle cx="12" cy="9.5" r="1.6" fill="#f7c61d"/></svg><span><b>Locations</b>1420 Larkspur Rd, Fairview</span></div>
  </div>
  <div class="abs foot-rule"></div>
  <div class="abs foot-brand"><i class="dot"></i><span>Meadowlark</span></div>
  <div class="abs foot-col" style="left:380px"><h6>Quick Link</h6><ul><li>Home</li><li>Services</li><li>Portfolio</li><li>Pages</li><li>News</li><li>Contact</li></ul></div>
  <div class="abs foot-col" style="left:580px"><h6>Quick Link</h6><ul><li>Exterior Hand Dry</li><li>Express Interior Vacuum</li><li>Rubber Mats Refresh</li><li>Door Jambs &amp; Windows</li><li>Interior Glass Cleaned</li></ul></div>
  <div class="abs foot-col" style="left:860px"><h6>Recent Post</h6>
    <div class="post"><div class="thumb" role="img" aria-label="Post photo of a clean car"></div><div><small>12 Apr 2024</small>Keep your car shining all season long</div></div>
    <div class="post"><div class="thumb" role="img" aria-label="Post photo of a wash tunnel"></div><div><small>02 Apr 2024</small>The bright choice for a fresh car</div></div>
  </div>
  <div class="abs copyright">Copyright © 2024. All Rights Reserved. Privacy Policy</div>
</footer>

</body>
</html>
```